Premium label design for product needed

UPDATE: (Scroll down)
For a face care product i need a new front label on the bottle. The current one is white and i want to add the franchise color green. The objective is to premiunize the packaging and to give guidance to the consumers to find their franchise color. The task is to find several option to color the label on the bottle in the most premium way. But at the same time it should not be playful, more in a serious medical direction or in a counterbrand direction. It should look absolutely premium. but should not shout to much. The text structure should remain the same. I will provide a powerpoint slide to illustrate the task even clearer.
UPDATE: DO NOT DESIGN THE FOLDING BOX, only design the bottle. The folding box only serves the purpose of giving the text/layout structure and rough color intent.

Target Market(s)

female 25-39

Requirements
Must have
• Premium, Uniqueness, Innovative

```html
<!DOCTYPE html>
<html lang="en">
<head>
<meta charset="UTF-8">
<title>Pure Skin Solution – Bottle Label</title>
<link href="https://fonts.googleapis.com/css2?family=Montserrat:wght@300;400;500;900&display=swap" rel="stylesheet">
<style>
  :root {
    --backdrop: #eef0ec;
    --franchise-green: #66dd5e;
    --franchise-green-deep: #3fc24f;
    --label-white: #ffffff;
    --ink: #111111;
    --brand-grey: #3a4250;
    --ring: #c9ced1;
  }
  * { margin: 0; padding: 0; box-sizing: border-box; }
  html, body {
    width: 1200px;
    height: 960px;
    overflow: hidden;
    background: var(--backdrop);
    font-family: "Montserrat", sans-serif;
  }
  .canvas {
    width: 1200px;
    height: 960px;
    display: flex;
    align-items: center;
    justify-content: center;
  }
  .bottle {
    width: 340px;
    height: 880px;
    display: flex;
    flex-direction: column;
    border-radius: 26px;
    overflow: hidden;
    box-shadow: 0 18px 40px rgba(0,0,0,0.12);
  }
  .bottle__cap {
    height: 270px;
    background: var(--franchise-green);
    border-radius: 26px 26px 0 0;
  }
  .bottle__ring {
    height: 8px;
    background: linear-gradient(var(--ring), #f4f6f7, var(--ring));
  }
  .bottle__body {
    flex: 1;
    background: var(--label-white);
    display: flex;
    flex-direction: column;
  }
  .brand {
    height: 170px;
    display: flex;
    align-items: center;
    justify-content: center;
    gap: 12px;
  }
  .brand__dot {
    width: 22px;
    height: 22px;
    border-radius: 50%;
    background: var(--franchise-green-deep);
  }
  .brand__name {
    font-weight: 500;
    font-size: 26px;
    letter-spacing: 2px;
    color: var(--brand-grey);
  }
  .product-band {
    height: 200px;
    background: linear-gradient(180deg, var(--franchise-green) 0%, var(--franchise-green-deep) 100%);
    display: flex;
    flex-direction: column;
    justify-content: center;
    padding-left: 34px;
    color: var(--ink);
    line-height: 1.02;
  }
  .product-band__line1 {
    font-weight: 900;
    font-size: 48px;
    letter-spacing: 0.5px;
  }
  .product-band__line2 {
    font-weight: 300;
    font-size: 48px;
    letter-spacing: 1px;
  }
  .variant {
    flex: 1;
    padding: 44px 0 0 34px;
    font-weight: 400;
    font-size: 22px;
    letter-spacing: 1px;
    color: var(--ink);
  }
  .range-strip {
    height: 40px;
    background: var(--franchise-green-deep);
    display: flex;
    align-items: center;
    justify-content: center;
    color: var(--label-white);
    font-weight: 400;
    font-size: 17px;
    letter-spacing: 1.5px;
  }
</style>
</head>
<body>
  <main class="canvas">
    <div class="bottle">
      <div class="bottle__cap"></div>
      <div class="bottle__ring"></div>
      <div class="bottle__body">
        <div class="brand">
          <span class="brand__dot"></span>
          <span class="brand__name">Verdelle</span>
        </div>
        <div class="product-band">
          <span class="product-band__line1">PURE SKIN</span>
          <span class="product-band__line2">SOLUTION</span>
        </div>
        <p class="variant">A.I. MATT FLUID</p>
        <div class="range-strip">DERMATOLOGICAL SKINCARE</div>
      </div>
    </div>
  </main>
</body>
</html>
```